Swing Dance Themed Cleaning Company Website

We need a website designed for a cleaning company based in Portland, Oregon called Bellhop Sweep. We clean homes and commercial buildings, inside and out.

needs to be vintage and like the velvet marlow. Speakeasy 1920s feel.
needs to be classy.

Check out bellhopsweep.com We are not happy with the site currently.

please look at house finderly site for more content https://www.housefinderly.com/rated.BellhopSweepCleaning.48217065.html

Check out my videos on my ClipHarbor channel Bellhop Sweep

Target Market(s)

middle class and home owner

Industry/Entity Type

Cleaning Service

Number of Pages Required

3 page

Font styles to use
Other font styles liked:
• jazzrag

Colors

Designer to choose colors to be used in the design.

Requirements
Must have
• must be good on pc and mobile

```html
<!DOCTYPE html>
<html lang="en">
<head>
<meta charset="utf-8">
<title>Bellhop Sweep – Keep Cleaning Classy Portland</title>
<link rel="stylesheet" href="https://fonts.googleapis.com/css2?family=Poiret+One&family=Roboto+Condensed:wght@400;700&display=swap">
<style>
:root{
  --olive:#6d6a3c;
  --yellow:#f6ee3c;
  --ink:#1f2230;
  --navy:#2d3142;
  --orange:#e05a28;
  --nav-bg:#f3f3f3;
  --white:#ffffff;
  --muted:#6a6d78;
  --sans:"Roboto Condensed",Arial,sans-serif;
  --deco:"Poiret One",Georgia,serif;
}
*{box-sizing:border-box;margin:0;padding:0}
html,body{width:702px;height:1200px;overflow:hidden;background:var(--white)}
.page{position:relative;width:702px;height:1200px;font-family:var(--sans);color:var(--ink)}
.abs{position:absolute}

/* hero */
.hero{left:0;top:0;width:702px;height:289px;background:linear-gradient(90deg,#5e5c3e 0%,#8a8a3a 40%,#c9c83a 70%,var(--yellow) 100%)}
.brand{left:94px;top:22px;display:flex;align-items:center;gap:5px}
.brand-mark{width:22px;height:22px;background:var(--yellow)}
.brand-name{font-family:var(--sans);font-weight:700;color:var(--yellow);font-size:15px;line-height:14px;text-transform:uppercase;width:80px}
.brand-tag{left:94px;top:59px;font-size:6px;color:var(--yellow);text-transform:uppercase;letter-spacing:.2px}
.hero-title{left:92px;top:126px;font-family:var(--deco);font-weight:400;color:var(--yellow);font-size:38px;line-height:48px;text-transform:uppercase}
.hero-rule{height:5px;background:var(--white)}
.hero-art{left:380px;top:18px;width:230px;height:232px;border-radius:8px;background:radial-gradient(circle at 50% 55%,rgba(240,160,150,.55),rgba(200,220,180,.35) 60%,transparent 75%)}
.play{left:482px;top:117px;width:50px;height:50px;border:2px solid var(--white);border-radius:50%}
.play::after{content:"";position:absolute;left:19px;top:15px;border-left:14px solid var(--white);border-top:9px solid transparent;border-bottom:9px solid transparent}

/* nav */
.nav{left:0;top:289px;width:702px;height:27px;background:var(--nav-bg)}
.nav-links{left:94px;top:0;height:27px;display:flex;align-items:center;gap:18px;font-size:7px;font-weight:700;text-transform:uppercase;list-style:none}
.nav-icons{left:451px;top:9px;display:flex;gap:10px}
.nav-icons span{width:9px;height:9px;border:1.5px solid #5b7fc0;border-radius:2px}
.nav-icons .search{border-color:var(--ink);border-radius:50%}
.lang{left:536px;top:0;width:71px;height:27px;background:var(--ink);color:var(--white);font-size:7px;font-weight:700;display:flex;align-items:center;justify-content:center;gap:8px;text-transform:uppercase}
.lang::after{content:"";border-top:4px solid var(--white);border-left:3px solid transparent;border-right:3px solid transparent}

/* about */
.about{left:0;top:316px;width:702px;height:152px;background:var(--orange);color:var(--white);text-align:center}
.about-art{left:0;top:8px;width:150px;height:144px;background:linear-gradient(135deg,rgba(0,0,0,.18),rgba(0,0,0,.05))}
.section-title{font-family:var(--deco);font-weight:400;font-size:22px;text-transform:uppercase;letter-spacing:.5px}
.about .section-title{position:absolute;left:0;width:702px;top:22px}
.rule-line{height:1px;background:currentColor}
.about p{position:absolute;left:0;width:702px;font-size:6.5px;line-height:10px}

/* services slider */
.slider{left:0;top:468px;width:702px;height:249px;background:var(--white)}
.slide{top:0;height:249px}
.slide-side-l{left:0;width:128px;background:linear-gradient(180deg,#6a3a4a,#4a2a40)}
.slide-main{left:129px;width:443px;background:linear-gradient(180deg,#5d5a55,#4e3c40 60%,#5a3b40)}
.slide-side-r{left:574px;width:128px;background:linear-gradient(180deg,#4e4450,#5a4a48)}
.arrow-btn{width:21px;height:21px;border:1px solid var(--white);background:rgba(0,0,0,.2)}
.arrow-btn::after{content:"";position:absolute;left:7px;top:6px;border-top:4px solid transparent;border-bottom:4px solid transparent}
.arrow-left::after{border-right:5px solid var(--white)}
.arrow-right::after{border-left:5px solid var(--white)}
.slide-title{left:154px;top:152px;font-family:var(--deco);font-weight:400;color:var(--white);font-size:27px;text-transform:uppercase}
.slide-btn{left:156px;top:194px;width:140px;height:20px;border:1px solid var(--white);color:var(--white);font-size:6.5px;font-weight:700;text-transform:uppercase;display:flex;align-items:center;padding-left:13px}
.slide-btn::after{content:"";position:absolute;right:0;top:0;width:20px;height:18px;border-left:1px solid var(--white)}
.slide-btn i{position:absolute;right:7px;top:6px;border-left:5px solid var(--white);border-top:3.5px solid transparent;border-bottom:3.5px solid transparent}

/* blogs */
.blogs-title{left:0;top:748px;width:702px;text-align:center;color:var(--ink)}
.blogs-bar{left:327px;top:784px;width:49px;height:5px;background:var(--navy)}
.blog-card{left:190px;top:824px;width:306px;height:166px;border:2px solid var(--ink);border-left:none;background:var(--white)}
.blog-shadow{left:200px;top:975px;width:288px;height:17px;background:var(--ink)}
.blog-portrait{left:96px;top:840px;width:100px;height:158px;background:linear-gradient(180deg,#f1f1f1,#e2e2e2)}
.blog-heading{left:203px;top:861px;display:flex;align-items:center;gap:4px;font-size:10px;font-weight:700}
.blog-heading::after{content:"";width:30px;height:2px;background:var(--ink)}
.blog-body{left:203px;top:884px;width:270px;font-size:6.2px;line-height:10.5px;color:var(--muted)}
.blog-more{left:203px;top:931px;font-size:5.5px;font-weight:700;text-transform:uppercase}
.sweeper-art{left:530px;top:905px;width:156px;height:142px;background:linear-gradient(160deg,#f2f2f2,#e4e4e4)}

/* footer */
.footer{left:0;top:1047px;width:702px;height:153px;background:var(--navy);color:var(--white)}
.footer .brand{top:32px}
.footer-address{left:94px;top:69px;font-size:5.6px;line-height:9px}
.footer-contact{left:94px;top:93px;font-size:5.6px;line-height:9px}
.footer-copy{left:94px;top:116px;font-size:5.6px}
.footer-divider{top:32px;width:2px;height:92px;background:var(--yellow)}
.footer-links{left:329px;top:36px;list-style:none;font-size:6px;font-weight:700;color:var(--yellow);line-height:12.3px;text-transform:uppercase}
.reach-title{left:460px;top:37px;font-size:6.5px;font-weight:700;color:var(--yellow);text-transform:uppercase}
.contact-form{left:460px;top:55px;width:132px}
.field{display:flex;align-items:center;width:132px;height:17px;border:1px solid var(--yellow);border-top-width:0;font-size:5.6px;font-style:italic;color:var(--white);padding-left:7px}
.field:first-child{border-top-width:1px}
.submit{display:flex;align-items:center;justify-content:center;width:132px;height:18px;background:var(--yellow);color:var(--ink);font-size:6.5px;font-weight:700;text-transform:uppercase}
</style>
</head>
<body>
<div class="page">

  <header class="hero abs">
    <div class="brand abs"><span class="brand-mark"></span><span class="brand-name">Bellhop Sweep</span></div>
    <div class="brand-tag abs">Keep cleaning classy Portland</div>
    <h1 class="hero-title abs">Bellhop Sweep<br>Keep Cleaning</h1>
    <div class="hero-rule abs" style="left:94px;top:171px;width:210px"></div>
    <div class="hero-rule abs" style="left:94px;top:219px;width:228px"></div>
    <div class="hero-art abs" role="img" aria-label="Illustration of a cheerful woman in an apron mopping a wet floor"></div>
    <div class="play abs" aria-label="Play video"></div>
  </header>

  <nav class="nav abs">
    <ul class="nav-links abs"><li>Home</li><li>About Us</li><li>Our Services</li><li>Blogs</li><li>Contact Us</li></ul>
    <div class="nav-icons abs"><span class="search"></span><span></span><span></span><span></span></div>
    <div class="lang abs">Language</div>
  </nav>

  <section class="about abs">
    <div class="about-art abs" role="img" aria-label="Sketch of a 1920s bellhop sweeping with a mop"></div>
    <div class="rule-line abs" style="left:130px;top:36px;width:96px"></div>
    <div class="rule-line abs" style="left:476px;top:36px;width:96px"></div>
    <h2 class="section-title">About Bellhop Sweep</h2>
    <p style="top:60px;font-weight:700">Making the greater Portland area clean, one building at a time</p>
    <p style="top:76px;font-weight:700">Good people, great service</p>
    <p style="top:97px">Bellhop Sweep is a family owned professional cleaning business. We provide our years of cleaning experience<br>to homes and businesses in and around Portland, Oregon.</p>
  </section>

  <section class="slider abs">
    <div class="slide slide-side-l abs" role="img" aria-label="Illustration of a housekeeper with a vacuum cleaner"></div>
    <div class="slide slide-main abs" role="img" aria-label="Illustration of a woman vacuuming a living room carpet"></div>
    <div class="slide slide-side-r abs" role="img" aria-label="Illustration of a worker cleaning a building exterior on a ladder"></div>
    <div class="arrow-btn arrow-left abs" style="left:66px;top:114px"></div>
    <div class="arrow-btn arrow-right abs" style="left:614px;top:114px"></div>
    <h3 class="slide-title abs">General House Keeping</h3>
    <div class="slide-btn abs">Learn more about service<i></i></div>
  </section>

  <section>
    <div class="rule-line abs" style="left:94px;top:770px;width:150px;color:var(--ink)"></div>
    <div class="rule-line abs" style="left:458px;top:770px;width:150px;color:var(--ink)"></div>
    <h2 class="section-title blogs-title abs">Latest Blogs</h2>
    <div class="blogs-bar abs"></div>

    <div class="blog-shadow abs"></div>
    <article class="blog-card abs"></article>
    <div class="blog-portrait abs" role="img" aria-label="Sketch of a smiling 1920s woman with curled hair"></div>
    <h3 class="blog-heading abs">Bellhop Sweep Returns to Riverbank Swing Festival 2017</h3>
    <p class="blog-body abs">Bellhop Sweep returns to the Riverbank Swing Festival this June 30 through July 4, 2017. Say hi to us as we run a kids crafts booth. Bellhop Sweep returns to the Riverbank Swing Festival this June 30 through July 4, 2017. Say hi to us as we run a kids crafts booth.</p>
    <div class="blog-more abs">Learn more</div>
    <div class="sweeper-art abs" role="img" aria-label="Sketch of a bellhop sweeping with a mop"></div>
  </section>

  <footer class="footer abs">
    <div class="brand abs"><span class="brand-mark"></span><span class="brand-name">Bellhop Sweep</span></div>
    <div class="rule-line abs" style="left:185px;top:47px;width:100px;color:#6a6e80"></div>
    <div class="footer-address abs">418 NE Alder Ave #210, Portland,<br>OR 97232</div>
    <div class="footer-contact abs">503-555-0148<br>dan@bellhopsweep.com</div>
    <div class="footer-copy abs">© Copyright 2018 Bellhop Sweep, All Rights Reserved.</div>
    <div class="footer-divider abs" style="left:319px"></div>
    <ul class="footer-links abs"><li>Home</li><li>About Us</li><li>Services</li><li>Blogs</li><li>Contact Us</li></ul>
    <div class="footer-divider abs" style="left:449px"></div>
    <div class="reach-title abs">Reach Out</div>
    <div class="rule-line abs" style="left:500px;top:41px;width:95px;color:#6a6e80"></div>
    <form class="contact-form abs">
      <div class="field">Enter Your Name</div>
      <div class="field">Enter Your Email</div>
      <div class="field">Type Your Message</div>
      <div class="submit">Submit</div>
    </form>
  </footer>

</div>
</body>
</html>
```